Flyer Design for Tech Services Division

We provide technical services from server and computer repair to low voltage structured cabling and telephony wiring and support. We have W-2/employed field technicians (as opposed to independent contractors) in multiple states that we send out to provid

```html
<!DOCTYPE html>
<html lang="en">
<head>
<meta charset="UTF-8">
<title>On-site Technicians Flyer</title>
<link rel="stylesheet" href="https://fonts.googleapis.com/css2?family=Archivo+Black&family=Roboto+Slab:wght@700&display=swap">
<style>
  :root {
    --ink: #111111;
    --body-ink: #2e2e2e;
    --services-fill: #9a9a9a;
    --services-edge: #5a5a5a;
    --bg-light: #fbfbfb;
    --bg-mid: #d6d6d6;
    --bg-dark: #8e8e8e;
    --stripe: #e2e2e2;
    --bar: #a9a9a9;
  }
  html, body {
    margin: 0;
    padding: 0;
    width: 928px;
    height: 1200px;
    overflow: hidden;
    background: #ffffff;
  }
  .flyer {
    position: relative;
    width: 928px;
    height: 1200px;
    overflow: hidden;
    background: linear-gradient(150deg, var(--bg-light) 0%, var(--bg-light) 22%, var(--bg-mid) 55%, var(--bg-dark) 100%);
    font-family: "Roboto Slab", Georgia, serif;
    color: var(--ink);
  }
  .decor {
    position: absolute;
    left: 0;
    top: 0;
  }
  .headline {
    position: absolute;
    margin: 0;
    font-family: "Archivo Black", "Arial Black", sans-serif;
    font-weight: 400;
    color: var(--ink);
    white-space: nowrap;
    line-height: 1;
  }
  .headline--offer {
    left: 168px;
    top: 50px;
    font-size: 42px;
    letter-spacing: 0.2px;
  }
  .headline--price {
    left: 165px;
    top: 122px;
    font-size: 68px;
  }
  .website {
    position: absolute;
    left: 48px;
    top: 492px;
    transform: translate(-50%, -50%) rotate(-90deg);
    font-family: "Archivo Black", "Arial Black", sans-serif;
    font-size: 27px;
    color: var(--ink);
    white-space: nowrap;
    line-height: 1;
  }
  .services-title {
    position: absolute;
    left: 118px;
    top: 500px;
    transform: translate(-50%, -50%) rotate(-90deg);
    font-family: "Archivo Black", "Arial Black", sans-serif;
    font-size: 104px;
    color: var(--services-fill);
    -webkit-text-stroke: 2px var(--services-edge);
    letter-spacing: 1px;
    white-space: nowrap;
    line-height: 1;
  }
  .service-list {
    position: absolute;
    top: 296px;
    margin: 0;
    padding: 0;
    list-style: none;
    font-size: 25px;
    font-weight: 700;
    color: var(--body-ink);
  }
  .service-list li {
    height: 75.5px;
    line-height: 1.2;
    white-space: nowrap;
  }
  .service-list--left { left: 198px; }
  .service-list--right { left: 536px; font-size: 24.5px; }
  .service-list .indent { padding-left: 8px; }
  .call-to-action {
    position: absolute;
    left: 38px;
    top: 806px;
    margin: 0;
    font-family: "Archivo Black", "Arial Black", sans-serif;
    font-weight: 400;
    font-size: 33px;
    color: #3a3a3a;
    line-height: 54px;
    white-space: nowrap;
  }
  .call-to-action span { display: block; }
  .call-to-action .second { padding-left: 109px; }
  .mascot {
    position: absolute;
    left: 462px;
    top: 780px;
    width: 462px;
    height: 378px;
    border-radius: 40% 45% 30% 35%;
    background: radial-gradient(ellipse at 50% 45%, rgba(110,110,110,0.55) 0%, rgba(150,150,150,0.35) 55%, rgba(150,150,150,0) 75%);
  }
  .credentials {
    position: absolute;
    left: 33px;
    top: 1162px;
    margin: 0;
    font-family: "Archivo Black", "Arial Black", sans-serif;
    font-size: 23px;
    color: var(--ink);
    white-space: nowrap;
    line-height: 1;
  }
</style>
</head>
<body>
<main class="flyer">
  <svg class="decor" width="928" height="1200" viewBox="0 0 928 1200" aria-hidden="true">
    <polygon points="0,60 60,0 110,0 0,110" fill="var(--stripe)"/>
    <polygon points="0,150 150,0 205,0 0,205" fill="var(--stripe)"/>
    <rect x="12" y="0" width="14" height="1168" fill="var(--bar)"/>
  </svg>

  <h1 class="headline headline--offer">On - site technicians available</h1>
  <p class="headline headline--price">@ Just $49 per hour</p>

  <div class="website">www.FieldTechCrewPro.com</div>
  <div class="services-title">SERVICES</div>

  <ul class="service-list service-list--left">
    <li>Server/PC Repair</li>
    <li>Network Wiring</li>
    <li>Structured Cabling</li>
    <li>Telephone Wiring</li>
    <li>Hardware Deployment</li>
    <li>Printer Repair</li>
  </ul>

  <ul class="service-list service-list--right">
    <li>System Design</li>
    <li>Linux Server Administration</li>
    <li>Anti-Virus/Anti-Spyware</li>
    <li>User Touching</li>
    <li>Onsite Computer Training</li>
    <li>Supplementary Tech staffs<br><span class="indent">for large projects</span></li>
  </ul>

  <p class="call-to-action">
    <span>Ring Us &amp;</span>
    <span class="second">We will be on time</span>
  </p>

  <div class="mascot" role="img" aria-label="Cartoon of a cheerful technician in a checked vest striding forward, checking his watch"></div>

  <p class="credentials">"Virginia Contractor -- Licensed &amp; Insured"</p>
</main>
</body>
</html>
```